KGDB Business Card

Looking for a business card design to incorporate our branding. We want to only use the colors listing in the Branding Package (attached).
Updates

Target Market(s)

People who need their phone or device fixed.

Industry/Entity Type

Electronics

Contact Information for Business Card

Please use:

Bright Circuit Mending Depot LLC
3478 S Ridge Trail 2210 E
Suite 417
San Antonio, TX 78341

Marcus Delwyn, Store Manager

(210) 555-0143

Requirements
Must have
• Must include the colors that are contained within the Branding Package PDF file.

```html
<!DOCTYPE html>
<html lang="en">
<head>
<meta charset="utf-8">
<title>KGDB Business Card</title>
<link href="https://fonts.googleapis.com/css2?family=Lato:wght@400;700&display=swap" rel="stylesheet">
<style>
  :root {
    --brand-orange: #ff5100;
    --paper: #ffffff;
    --ink: #3a3a3a;
    --backdrop: #ececec;
  }
  * { margin: 0; padding: 0; box-sizing: border-box; }
  html, body { width: 1200px; height: 1200px; overflow: hidden; }
  body {
    background: var(--backdrop);
    font-family: "Lato", sans-serif;
    position: relative;
  }
  .card {
    position: absolute;
    left: 180px;
    width: 840px;
    height: 480px;
    overflow: hidden;
  }
  .card--front { top: 90px; background: var(--brand-orange); }
  .card--back { top: 630px; background: var(--paper); }

  .edge-bar { position: absolute; width: 8px; }
  .card--front .edge-bar { background: var(--paper); }
  .card--back .edge-bar { background: var(--brand-orange); }
  .edge-bar--left { left: 26px; }
  .edge-bar--right { right: 26px; }
  .card--front .edge-bar--left { top: 230px; height: 220px; }
  .card--front .edge-bar--right { top: 30px; height: 200px; }
  .card--back .edge-bar--left { top: 250px; height: 210px; }
  .card--back .edge-bar--right { top: 30px; height: 210px; }

  .wordmark {
    position: absolute;
    display: flex;
    align-items: center;
    gap: 14px;
    font-weight: 700;
    white-space: nowrap;
  }
  .wordmark__square { width: 34px; height: 34px; border-radius: 6px; }
  .card--front .wordmark {
    left: 50%; top: 50%;
    transform: translate(-50%, -50%);
    color: var(--paper);
    font-size: 38px;
  }
  .card--front .wordmark__square { background: var(--paper); }
  .card--back .wordmark {
    left: 80px; bottom: 110px;
    color: var(--brand-orange);
    font-size: 26px;
  }
  .card--back .wordmark__square { width: 26px; height: 26px; background: var(--brand-orange); }

  .identity {
    position: absolute;
    right: 80px;
    top: 70px;
    width: 380px;
  }
  .identity__name {
    color: var(--brand-orange);
    font-weight: 700;
    font-size: 34px;
    letter-spacing: 0.5px;
    text-transform: uppercase;
  }
  .identity__title {
    color: var(--ink);
    font-size: 22px;
    padding-bottom: 10px;
    border-bottom: 2px solid var(--brand-orange);
  }
  .contact { list-style: none; margin-top: 24px; }
  .contact__item {
    display: flex;
    gap: 12px;
    color: var(--ink);
    font-size: 19px;
    line-height: 1.35;
    margin-bottom: 12px;
  }
  .contact__icon { flex: 0 0 20px; height: 20px; margin-top: 3px; }
</style>
</head>
<body>
  <section class="card card--front" aria-label="Business card front">
    <span class="edge-bar edge-bar--left"></span>
    <span class="edge-bar edge-bar--right"></span>
    <div class="wordmark"><span class="wordmark__square"></span>Bright Circuit Mending Depot</div>
  </section>

  <section class="card card--back" aria-label="Business card back">
    <span class="edge-bar edge-bar--left"></span>
    <span class="edge-bar edge-bar--right"></span>

    <div class="identity">
      <h1 class="identity__name">Marcus Delwyn</h1>
      <p class="identity__title">Store Manager</p>
      <ul class="contact">
        <li class="contact__item">
          <svg class="contact__icon" viewBox="0 0 20 20" aria-hidden="true">
            <rect width="20" height="20" rx="3" fill="#ff5100"/>
            <path d="M10 4a4 4 0 0 0-4 4c0 3 4 8 4 8s4-5 4-8a4 4 0 0 0-4-4z" fill="#fff"/>
            <circle cx="10" cy="8" r="1.5" fill="#ff5100"/>
          </svg>
          <span>3478 S Ridge Trail 2210 E<br>Suite 417<br>San Antonio, TX 78341</span>
        </li>
        <li class="contact__item">
          <svg class="contact__icon" viewBox="0 0 20 20" aria-hidden="true">
            <rect width="20" height="20" rx="3" fill="#ff5100"/>
            <path d="M6 4h3l1 3-2 1.5a8 8 0 0 0 3.5 3.5L13 10l3 1v3c0 1-1 2-2 2A10 10 0 0 1 4 6c0-1 1-2 2-2z" fill="#fff"/>
          </svg>
          <span>(210) 555-0143</span>
        </li>
      </ul>
    </div>

    <div class="wordmark"><span class="wordmark__square"></span>Bright Circuit Mending Depot</div>
  </section>
</body>
</html>
```